3 out of 100 people will get deadly skin cancer - we need a great illustration that shows this!

We put together a prototype image that communicates lifetime skin cancer risk. (see attached). We are looking for illustrators who can take make a new/better/cooler graphic that communicates this idea. It could be as simple as a superior illustration of the graphic we have or illustrators can propose a completely different idea.What should the illustration communicate?U.S. adults have a lifetime risk of developing skin cancer of 1 in 5. But we don't want to show 1 in 5; we want to show that number in a larger group. For example, in the attached illustration we show 20 in 100 people get skin cancer (i.e., 100 beach towels/umbrellas and 20 of them are red). Research has shown that people are more likely to accurately understand numbers like this when you convey them for larger groups (i.e., 20 out of 100 rather than 1 out of 5). U.S. adults also have a lifetime risk of 2.3% of developing the deadliest form of skin cancer (melanoma). In other words, approximately 3 in 100 people will develop melanoma in their lifetime. Ideally, a single image will convey both lifetime skin cancer risk (20 in 100) and melanoma risk (3 in 100). We will award a top three as follows: 1st place = $300, 2nd place = $250, third place = $200. We will also buy any design beyond 3rd place that we like for $100. For example, we purchased 24 designs in our last contest on Artmarketly.This research is supported by funding from the Corvane Institute of Science.

Target Market(s)

The U.S. public; individuals at high risk of developing skin cancer

Industry/Entity Type

Medicine

Colors

Designer to choose colors to be used in the design.

Requirements
Must have
• an original illustration that conveys both lifetime risk of developing skin cancer (20 in 100) and melanoma (3 in 100).
Nice to have
• It can be beach towels and umbrellas, just like our prototype, or the designers can pitch an original idea. Imagery can be realistic or cartoonish (or something in between). It should be illustrations, though. Not edited photos. The image should be in color (no black and white illustrations).
Should not have
• Photos. Clip art. Free vector images.
• We are looking for original illustrations created by the designer.

```html
<!DOCTYPE html>
<html lang="en">
<head>
<meta charset="utf-8">
<title>How likely are you to get skin cancer?</title>
<link rel="stylesheet" href="https://fonts.googleapis.com/css2?family=Didact+Gothic&display=swap">
<style>
  :root {
    --paper: #e4f2ec;
    --ink: #2b2b2b;
    --sun-orange: #f0a040;
    --sun-deep: #d9782a;
    --jungle: #3f6b2a;
    --water-top: #3fcaa9;
    --water-bottom: #2b9c8e;
    --badge: #8edbc9;
    --cream: #f1e8d8;
    --umbrella-red: #d8352a;
    --lounger-dark: #3c3a2c;
    --pole: #8a7a66;
  }
  html, body { margin: 0; padding: 0; overflow: hidden; }
  body { width: 1200px; height: 3088px; background: var(--paper); }
  .poster {
    position: relative; width: 1200px; height: 3088px; overflow: hidden;
    background: var(--paper);
    font-family: "Didact Gothic", "Century Gothic", sans-serif;
    color: var(--ink);
  }
  .poster__title {
    position: absolute; top: 62px; left: 0; width: 100%;
    margin: 0; text-align: center; font-weight: 400;
    font-size: 36px; letter-spacing: 1px; text-decoration: underline;
    text-underline-offset: 6px;
  }
  .poster__lead {
    position: absolute; top: 158px; left: 0; width: 100%;
    margin: 0; text-align: center; font-size: 28px; letter-spacing: 3px;
    font-variant: small-caps;
  }
  .poster__question {
    position: absolute; top: 262px; left: 84px; width: 1060px;
    margin: 0; font-size: 40px; line-height: 1.35; text-transform: uppercase;
    letter-spacing: 0.5px;
  }
  .legend { position: absolute; top: 452px; left: 170px; margin: 0; padding: 0; list-style: none; }
  .legend__item { display: flex; align-items: center; height: 100px; }
  .legend__icon { width: 90px; height: 90px; margin-right: 20px; }
  .legend__label { font-size: 62px; letter-spacing: 4px; text-transform: uppercase; }
  .legend__label--spaced { letter-spacing: 16px; }
  .beach-scene {
    position: absolute; top: 790px; left: 0; width: 1200px; height: 1060px;
    background: linear-gradient(180deg, var(--sun-orange) 0%, var(--sun-deep) 40%, var(--jungle) 72%, #e9b870 100%);
  }
  .water {
    position: absolute; top: 1850px; left: 0; width: 1200px; height: 1238px;
    background: linear-gradient(180deg, var(--water-top), var(--water-bottom));
  }
  .pictogram { position: absolute; top: 0; left: 0; }
</style>
</head>
<body>
<main class="poster">
  <svg width="0" height="0" style="position:absolute">
    <defs>
      <symbol id="spot-clear" viewBox="0 0 80 80">
        <circle cx="40" cy="40" r="38" fill="var(--badge)" opacity="0.75"/>
        <line x1="40" y1="24" x2="40" y2="58" stroke="var(--pole)" stroke-width="2.5"/>
        <path d="M16 30 Q40 6 64 30 Z" fill="var(--cream)"/>
        <rect x="22" y="52" width="38" height="8" rx="3" fill="var(--cream)"/>
      </symbol>
      <symbol id="spot-cancer" viewBox="0 0 80 80">
        <circle cx="40" cy="40" r="38" fill="var(--badge)" opacity="0.75"/>
        <line x1="40" y1="24" x2="40" y2="58" stroke="var(--pole)" stroke-width="2.5"/>
        <path d="M16 30 Q40 6 64 30 Z" fill="var(--umbrella-red)"/>
        <rect x="22" y="52" width="38" height="8" rx="3" fill="var(--cream)"/>
      </symbol>
      <symbol id="spot-melanoma" viewBox="0 0 80 80">
        <circle cx="40" cy="40" r="38" fill="var(--badge)" opacity="0.75"/>
        <line x1="40" y1="24" x2="40" y2="58" stroke="var(--pole)" stroke-width="2.5"/>
        <path d="M16 30 Q40 6 64 30 Z" fill="var(--umbrella-red)"/>
        <rect x="22" y="52" width="38" height="8" rx="3" fill="var(--lounger-dark)"/>
      </symbol>
    </defs>
  </svg>

  <h1 class="poster__title">How likely are you to get skin cancer?</h1>
  <p class="poster__lead">Let's say 100 people go to the beach . . .</p>
  <p class="poster__question">How many will develop skin cancer in their lifetime? How many will develop melanoma, the deadliest form of skin cancer?</p>

  <ul class="legend">
    <li class="legend__item"><svg class="legend__icon"><use href="#spot-clear"/></svg><span class="legend__label">- No skin cancer</span></li>
    <li class="legend__item"><svg class="legend__icon"><use href="#spot-cancer"/></svg><span class="legend__label">- Skin cancer</span></li>
    <li class="legend__item"><svg class="legend__icon"><use href="#spot-melanoma"/></svg><span class="legend__label legend__label--spaced">- Melanoma</span></li>
  </ul>

  <div class="beach-scene" role="img" aria-label="Illustrated tropical beach: orange mountains, palm trees and a round thatched beach hut on a wooden deck"></div>

  <section class="water">
    <svg class="pictogram" width="1200" height="1238" viewBox="0 0 1200 1238" role="img" aria-label="100 beach spots: 80 with cream umbrellas, 17 with red umbrellas, 3 with red umbrellas and dark loungers">
      <g transform="translate(80 40)">
        <!-- row 0 -->
        <use href="#spot-clear" x="0" y="0" width="80" height="80"/><use href="#spot-clear" x="106" y="0" width="80" height="80"/><use href="#spot-cancer" x="212" y="0" width="80" height="80"/><use href="#spot-clear" x="318" y="0" width="80" height="80"/><use href="#spot-clear" x="424" y="0" width="80" height="80"/><use href="#spot-clear" x="530" y="0" width="80" height="80"/><use href="#spot-clear" x="636" y="0" width="80" height="80"/><use href="#spot-cancer" x="742" y="0" width="80" height="80"/><use href="#spot-clear" x="848" y="0" width="80" height="80"/><use href="#spot-clear" x="954" y="0" width="80" height="80"/>
        <!-- row 1 -->
        <use href="#spot-clear" x="0" y="118" width="80" height="80"/><use href="#spot-clear" x="106" y="118" width="80" height="80"/><use href="#spot-clear" x="212" y="118" width="80" height="80"/><use href="#spot-melanoma" x="318" y="118" width="80" height="80"/><use href="#spot-clear" x="424" y="118" width="80" height="80"/><use href="#spot-cancer" x="530" y="118" width="80" height="80"/><use href="#spot-clear" x="636" y="118" width="80" height="80"/><use href="#spot-clear" x="742" y="118" width="80" height="80"/><use href="#spot-cancer" x="848" y="118" width="80" height="80"/><use href="#spot-clear" x="954" y="118" width="80" height="80"/>
        <!-- row 2 -->
        <use href="#spot-clear" x="0" y="236" width="80" height="80"/><use href="#spot-cancer" x="106" y="236" width="80" height="80"/><use href="#spot-clear" x="212" y="236" width="80" height="80"/><use href="#spot-clear" x="318" y="236" width="80" height="80"/><use href="#spot-clear" x="424" y="236" width="80" height="80"/><use href="#spot-clear" x="530" y="236" width="80" height="80"/><use href="#spot-clear" x="636" y="236" width="80" height="80"/><use href="#spot-cancer" x="742" y="236" width="80" height="80"/><use href="#spot-clear" x="848" y="236" width="80" height="80"/><use href="#spot-clear" x="954" y="236" width="80" height="80"/>
        <!-- row 3 -->
        <use href="#spot-clear" x="0" y="354" width="80" height="80"/><use href="#spot-clear" x="106" y="354" width="80" height="80"/><use href="#spot-cancer" x="212" y="354" width="80" height="80"/><use href="#spot-clear" x="318" y="354" width="80" height="80"/><use href="#spot-clear" x="424" y="354" width="80" height="80"/><use href="#spot-clear" x="530" y="354" width="80" height="80"/><use href="#spot-clear" x="636" y="354" width="80" height="80"/><use href="#spot-clear" x="742" y="354" width="80" height="80"/><use href="#spot-clear" x="848" y="354" width="80" height="80"/><use href="#spot-cancer" x="954" y="354" width="80" height="80"/>
        <!-- row 4 -->
        <use href="#spot-cancer" x="0" y="472" width="80" height="80"/><use href="#spot-clear" x="106" y="472" width="80" height="80"/><use href="#spot-clear" x="212" y="472" width="80" height="80"/><use href="#spot-clear" x="318" y="472" width="80" height="80"/><use href="#spot-clear" x="424" y="472" width="80" height="80"/><use href="#spot-cancer" x="530" y="472" width="80" height="80"/><use href="#spot-clear" x="636" y="472" width="80" height="80"/><use href="#spot-clear" x="742" y="472" width="80" height="80"/><use href="#spot-clear" x="848" y="472" width="80" height="80"/><use href="#spot-clear" x="954" y="472" width="80" height="80"/>
        <!-- row 5 -->
        <use href="#spot-clear" x="0" y="590" width="80" height="80"/><use href="#spot-clear" x="106" y="590" width="80" height="80"/><use href="#spot-clear" x="212" y="590" width="80" height="80"/><use href="#spot-clear" x="318" y="590" width="80" height="80"/><use href="#spot-cancer" x="424" y="590" width="80" height="80"/><use href="#spot-clear" x="530" y="590" width="80" height="80"/><use href="#spot-clear" x="636" y="590" width="80" height="80"/><use href="#spot-melanoma" x="742" y="590" width="80" height="80"/><use href="#spot-clear" x="848" y="590" width="80" height="80"/><use href="#spot-clear" x="954" y="590" width="80" height="80"/>
        <!-- row 6 -->
        <use href="#spot-clear" x="0" y="708" width="80" height="80"/><use href="#spot-clear" x="106" y="708" width="80" height="80"/><use href="#spot-clear" x="212" y="708" width="80" height="80"/><use href="#spot-cancer" x="318" y="708" width="80" height="80"/><use href="#spot-clear" x="424" y="708" width="80" height="80"/><use href="#spot-clear" x="530" y="708" width="80" height="80"/><use href="#spot-clear" x="636" y="708" width="80" height="80"/><use href="#spot-clear" x="742" y="708" width="80" height="80"/><use href="#spot-cancer" x="848" y="708" width="80" height="80"/><use href="#spot-clear" x="954" y="708" width="80" height="80"/>
        <!-- row 7 -->
        <use href="#spot-clear" x="0" y="826" width="80" height="80"/><use href="#spot-clear" x="106" y="826" width="80" height="80"/><use href="#spot-melanoma" x="212" y="826" width="80" height="80"/><use href="#spot-clear" x="318" y="826" width="80" height="80"/><use href="#spot-cancer" x="424" y="826" width="80" height="80"/><use href="#spot-clear" x="530" y="826" width="80" height="80"/><use href="#spot-clear" x="636" y="826" width="80" height="80"/><use href="#spot-clear" x="742" y="826" width="80" height="80"/><use href="#spot-clear" x="848" y="826" width="80" height="80"/><use href="#spot-clear" x="954" y="826" width="80" height="80"/>
        <!-- row 8 -->
        <use href="#spot-clear" x="0" y="944" width="80" height="80"/><use href="#spot-clear" x="106" y="944" width="80" height="80"/><use href="#spot-clear" x="212" y="944" width="80" height="80"/><use href="#spot-cancer" x="318" y="944" width="80" height="80"/><use href="#spot-clear" x="424" y="944" width="80" height="80"/><use href="#spot-clear" x="530" y="944" width="80" height="80"/><use href="#spot-clear" x="636" y="944" width="80" height="80"/><use href="#spot-clear" x="742" y="944" width="80" height="80"/><use href="#spot-clear" x="848" y="944" width="80" height="80"/><use href="#spot-clear" x="954" y="944" width="80" height="80"/>
        <!-- row 9 -->
        <use href="#spot-cancer" x="0" y="1062" width="80" height="80"/><use href="#spot-clear" x="106" y="1062" width="80" height="80"/><use href="#spot-clear" x="212" y="1062" width="80" height="80"/><use href="#spot-clear" x="318" y="1062" width="80" height="80"/><use href="#spot-clear" x="424" y="1062" width="80" height="80"/><use href="#spot-cancer" x="530" y="1062" width="80" height="80"/><use href="#spot-clear" x="636" y="1062" width="80" height="80"/><use href="#spot-clear" x="742" y="1062" width="80" height="80"/><use href="#spot-clear" x="848" y="1062" width="80" height="80"/><use href="#spot-clear" x="954" y="1062" width="80" height="80"/>
      </g>
    </svg>
  </section>
</main>
</body>
</html>
```